Where Quiet Rivers Carry Us

I have a previously designed book cover, and although I am mostly happy with it, I do not care for the photo on the cover of the book. I would like to keep the fonts and scrollwork on the current book cover (the brown outer edge is optional).
I prefer a Christian focus with a soft, gentle, grieving, trusting feeling of a mother as God leads without the typical religious symbols (ie: huge hands, overwhelming crosses, Heaven opening). Softly toned or small Christian icons would be acceptable.
The book dimensions are 5.5 X 8.5 and the spine is 1/2" thick.
Original book cover is here: http://wherequietriverscarryus.pinebrookpages.net/p/free-books.html
Back cover book description (two photos and the logo for the back cover can be found below) :
For I am the Lord your God who takes hold of your right hand and says to you, "Do not fear, I will help you." Isaiah 41:13
One day you were here, Colby, the next you were at the throne of God. How I long to know what heaven is like so I can envision where you are. Are you talking to Gideon about the battles of old? Are you asking Paul about the stonings, the scales, and the shipwrecks? Or are you still just standing in awe of the God and Savior that your mother could never have come close to describing to you? How I long to stand in awe with you, praising the God who gives and takes away. Just like I told you all those times when you were here with us, "If you go first, I'll see you when I get there, my son." Love you, Mom
On Friday, February 18, 2011, God did the unthinkable in our lives: He chose to take our 12-year-old son, Colby, home to heaven in a skiing accident. It is only considered the unthinkable because our plans are not God's plans and our ways are not God's ways. Follow along on my journey through the valley of the shadow of death as my Savior, Jesus Christ, leads me.
(Author info)
Janna L. Voskuilen lives on a small farm in northern Wisconsin with her husband, Dale, and their children. Experiencing the tragic death of her son has caused her to draw closer to God as He leads her down an unexpected path to know Him better.
I have updated the back cover details to include the exact words for the back cover as well as two photos and a logo. Thank you, designers, for sharing your creativity!
Reason: Still looking for the perfect book cover!
Reason: Still looking for the perfect design!
Working on final revisions!

```html
<!DOCTYPE html>
<html lang="en">
<head>
<meta charset="utf-8">
<title>Where Quiet Rivers Carry Us – Book Cover</title>
<link rel="stylesheet" href="https://fonts.googleapis.com/css2?family=Arvo&family=Pinyon+Script&family=Cinzel:wght@400;600&display=swap">
<style>
  :root {
    --sepia-dark: #2b1a10;
    --sepia-mid: #6b4a33;
    --sepia-light: #a88566;
    --sepia-glow: #c9ab8c;
    --spine-black: #0c0806;
    --text-light: #f3ece4;
    --title-silver: #e4ddd6;
    --author-dark: #24160d;
    --logo-paper: #dcdad6;
    --logo-ink: #1e1a16;
  }
  html, body {
    margin: 0;
    padding: 0;
    overflow: hidden;
    background: #ffffff;
  }
  .cover {
    position: relative;
    width: 1200px;
    height: 887px;
    overflow: hidden;
    font-family: "Arvo", Georgia, serif;
    background: var(--sepia-mid);
  }

  /* ---------- Back cover ---------- */
  .back-photo {
    position: absolute;
    left: 0; top: 0;
    width: 548px; height: 887px;
    background:
      radial-gradient(ellipse 60px 420px at 290px 440px, rgba(255,244,225,0.35), transparent 70%),
      radial-gradient(ellipse 320px 40px at 280px 410px, rgba(255,244,225,0.3), transparent 70%),
      radial-gradient(ellipse at 300px 300px, var(--sepia-light), var(--sepia-mid) 55%, var(--sepia-dark) 100%);
  }
  .back-frame {
    position: absolute;
    left: 0; top: 0;
  }
  .scroll-top {
    position: absolute;
    left: 45px; top: 6px;
    width: 470px; height: 50px;
    background: linear-gradient(90deg, transparent, rgba(255,255,255,0.35) 20%, rgba(255,255,255,0.45) 50%, rgba(255,255,255,0.35) 80%, transparent);
    border-radius: 25px;
    opacity: 0.6;
  }
  .back-text {
    position: absolute;
    left: 40px;
    width: 496px;
    color: var(--text-light);
    font-size: 13.6px;
    line-height: 23.3px;
    margin: 0;
  }
  .verse { top: 96px; }
  .letter { top: 155px; }
  .summary { top: 407px; }

  .author-photo {
    position: absolute;
    left: 32px; top: 566px;
    width: 130px; height: 176px;
    border: 3px solid var(--text-light);
    background: linear-gradient(160deg, var(--sepia-glow), var(--sepia-mid) 60%, var(--sepia-dark));
  }
  .logo-box {
    position: absolute;
    left: 32px; top: 757px;
    width: 134px; height: 65px;
    background: var(--logo-paper);
    display: flex;
    align-items: center;
    justify-content: center;
    text-align: center;
    color: var(--logo-ink);
    font-size: 14px;
    line-height: 18px;
    text-transform: uppercase;
  }
  .about-heading {
    position: absolute;
    left: 189px; top: 570px;
    margin: 0;
    font-weight: 400;
    font-size: 16px;
    line-height: 22px;
    color: var(--text-light);
    letter-spacing: 0.5px;
  }
  .about-text {
    position: absolute;
    left: 189px; top: 612px;
    width: 275px;
    margin: 0;
    color: var(--text-light);
    font-size: 13px;
    line-height: 20px;
  }
  .scroll-spine-side {
    position: absolute;
    left: 455px; top: 640px;
    width: 90px; height: 240px;
    background: radial-gradient(ellipse at 60% 60%, rgba(255,220,200,0.35), transparent 70%);
  }

  /* ---------- Spine ---------- */
  .spine {
    position: absolute;
    left: 548px; top: 0;
    width: 80px; height: 887px;
    background: var(--spine-black);
  }
  .spine-title {
    position: absolute;
    left: 18px; top: 22px;
    writing-mode: vertical-rl;
    font-family: "Pinyon Script", cursive;
    font-size: 33px;
    color: var(--text-light);
    white-space: nowrap;
  }
  .spine-author {
    position: absolute;
    left: 24px; top: 545px;
    writing-mode: vertical-rl;
    font-family: "Cinzel", serif;
    font-size: 21px;
    color: var(--text-light);
    white-space: nowrap;
  }

  /* ---------- Front cover ---------- */
  .front-photo {
    position: absolute;
    left: 628px; top: 0;
    width: 572px; height: 887px;
    background:
      radial-gradient(ellipse 230px 280px at 360px 600px, rgba(235,220,205,0.55), transparent 70%),
      radial-gradient(ellipse 180px 240px at 420px 200px, rgba(200,170,140,0.55), transparent 75%),
      linear-gradient(100deg, var(--sepia-dark) 0%, var(--sepia-mid) 45%, var(--sepia-light) 75%, var(--sepia-mid) 100%);
  }
  .scroll-front-top {
    position: absolute;
    left: 640px; top: 0;
    width: 130px; height: 90px;
    background: radial-gradient(ellipse at 40% 40%, rgba(30,15,8,0.45), transparent 70%);
  }
  .scroll-front-bottom {
    position: absolute;
    left: 630px; top: 690px;
    width: 110px; height: 190px;
    background: radial-gradient(ellipse at 50% 55%, rgba(30,15,8,0.45), transparent 70%);
  }
  .front-title {
    position: absolute;
    left: 672px; top: 92px;
    margin: 0;
    font-family: "Pinyon Script", cursive;
    font-weight: 400;
    font-size: 66px;
    line-height: 88px;
    color: var(--title-silver);
    text-shadow: 1px 1px 2px rgba(40,25,15,0.6);
  }
  .front-title span { display: block; }
  .front-title .line-2 { padding-left: 4px; }
  .front-author {
    position: absolute;
    left: 765px; top: 832px;
    margin: 0;
    font-family: "Cinzel", serif;
    font-size: 29px;
    font-weight: 400;
    color: var(--author-dark);
    white-space: nowrap;
  }
</style>
</head>
<body>
<div class="cover">

  <!-- Back cover -->
  <div class="back-photo" role="img" aria-label="Sepia church interior with pews and a soft light cross behind a faded portrait"></div>
  <div class="scroll-top" role="img" aria-label="Ornamental scrollwork across the top"></div>
  <svg class="back-frame" width="548" height="887" viewBox="0 0 548 887" aria-hidden="true">
    <polyline points="528,40 542,40 542,845" fill="none" stroke="#f3ece4" stroke-width="2"/>
  </svg>

  <p class="back-text verse">For I am the Lord your God who takes hold of your right and and says to you, "Do not fear, I will help you." Isaiah 41:13</p>
  <p class="back-text letter">One day you were here, Colby, the next you were at the throne of God. How I long to know what heaven's like so I can envision where you are. Are you talking to Gideon about the battles of old? Are you asking Paul about the stonings, the scales, and the shipwrecks? Or are you still just standing in awe of the God and Savior that your mother could never have come close to describing to you? How I long to stand in awe with you, praising the God who gives and takes away. Just like I told you all those times when you were here with us, "If you go first, I'll see you when I get there, my son." Love you, Mom</p>
  <p class="back-text summary">On Friday, February 18, 2011, God did the unthinkable in our lives: He chose to take our 12-year-old son, Colby, home to heaven in a skiing accident. It is only considered the unthinkable because our plans are not God's plans and our ways are not God's ways. Follow along on my journey through the valley of the shadow of death as my Savior, Jesus Christ, leads me.</p>

  <div class="author-photo" role="img" aria-label="Author portrait in a hat and plaid shirt"></div>
  <h2 class="about-heading">ABOUT THE AUTHOR</h2>
  <p class="about-text">Janna L. Voskuilen lives on a small farm in northern Wisconsin with her husband, Dale, and their children. Experiencing the tragic death of her son has caused her to draw closer to God as He leads her down an unexpected path to know Him better.</p>
  <div class="logo-box">Stillwater<br>Ministries</div>
  <div class="scroll-spine-side" role="img" aria-label="Glowing floral scrollwork"></div>

  <!-- Spine -->
  <div class="spine">
    <div class="spine-title">Where Quiet Rivers Carry Us</div>
    <div class="spine-author">JANNA L. VOSKUILEN</div>
  </div>

  <!-- Front cover -->
  <div class="front-photo" role="img" aria-label="Sepia portrait of a smiling boy in a backwards cap with folded praying hands in the foreground"></div>
  <div class="scroll-front-top" role="img" aria-label="Dark floral scrollwork in the top corner"></div>
  <div class="scroll-front-bottom" role="img" aria-label="Dark floral scrollwork in the lower corner"></div>
  <svg style="position:absolute;left:628px;top:0" width="572" height="887" viewBox="0 0 572 887" aria-hidden="true">
    <polyline points="302,17 557,17 557,300" fill="none" stroke="#24160d" stroke-width="2"/>
    <line x1="140" y1="857" x2="552" y2="857" stroke="#24160d" stroke-width="1.5"/>
  </svg>
  <h1 class="front-title"><span>Where Quiet</span><span class="line-2">Rivers</span><span>Carry Us</span></h1>
  <p class="front-author">JANNA L. VOSKUILEN</p>

</div>
</body>
</html>
```